Marrowind Exteriors

Design 2-3 branded image ads using all for provided logos. each ad is for a roof replacement. The offer is, buy a new roof and receive a free gutter replacement, and 10 years of free rood maintenance. These must be included. What's optional ? you have the option the mention 50 year warranty, 25 year workmanship warranty. You also have an option to use price offer of $17,997.

```html
<!DOCTYPE html>
<html lang="en">
<head>
<meta charset="utf-8">
<title>Marrowind Exteriors – New Roof Offer</title>
<link href="https://fonts.googleapis.com/css2?family=Montserrat:wght@300;700;800;900&display=swap" rel="stylesheet">
<style>
  :root {
    --stage: #cdec86;
    --ink-dark: #161616;
    --brand-red: #d71f27;
    --brand-green: #8cc63f;
    --white: #ffffff;
    --sky: #8fa3c4;
    --roof: #3b3d44;
    --rule: #cfcfcf;
    --badge-grey: #eeeeee;
    --badge-navy: #1d2f6f;
    --badge-gold: #c9a34a;
  }
  * { box-sizing: border-box; margin: 0; padding: 0; }
  html, body {
    width: 1200px; height: 849px; overflow: hidden;
    background: var(--stage);
    font-family: "Montserrat", sans-serif;
  }
  .flyer {
    position: absolute; left: 336px; top: 50px;
    width: 505px; height: 717px;
    background: var(--ink-dark);
    overflow: hidden;
  }
  .hero-photo {
    position: absolute; left: 0; top: 0; width: 505px; height: 340px;
    background: linear-gradient(180deg, var(--sky) 0%, #75849f 35%, var(--roof) 65%, var(--ink-dark) 100%);
  }
  .brand-flag { position: absolute; left: 49px; top: 0; width: 108px; height: 147px; }
  .brand-flag svg { position: absolute; inset: 0; }
  .brand-flag .brand-name {
    position: absolute; left: 0; width: 108px; top: 84px;
    text-align: center; color: var(--white);
    font-weight: 700; font-size: 10px; letter-spacing: 0.5px; line-height: 1.25;
  }
  .headline {
    position: absolute; left: 47px; top: 192px;
    color: var(--brand-green);
    font-weight: 900; font-size: 69px; line-height: 56px;
    letter-spacing: -0.5px; white-space: nowrap;
  }
  .exclaim { position: absolute; left: 303px; top: 191px; width: 46px; height: 171px; }
  .price-seal { position: absolute; left: 375px; top: 258px; width: 126px; height: 126px; }
  .rule { position: absolute; left: 49px; right: 0; height: 1px; background: var(--rule); }
  .rule--upper { top: 376px; }
  .rule--lower { top: 494px; }
  .offer {
    position: absolute; left: 47px; top: 382px;
    color: var(--white); font-size: 30px; line-height: 34px; font-weight: 300;
    letter-spacing: -0.3px; white-space: nowrap;
  }
  .offer strong, .warranty strong { font-weight: 700; }
  .warranty {
    position: absolute; left: 49px; top: 505px;
    color: var(--white); font-size: 21px; line-height: 24px; font-weight: 300;
    letter-spacing: -0.2px; white-space: nowrap;
  }
  .partner-strip {
    position: absolute; left: 0; bottom: 0; width: 505px; height: 105px;
    background: var(--white);
  }
  .partner { position: absolute; top: 19px; }
  .partner--brand {
    left: 49px; width: 86px; height: 65px; background: #111;
    display: flex; align-items: center; justify-content: center; text-align: center;
    color: var(--white); font-weight: 700; font-size: 7px; letter-spacing: 0.4px; line-height: 1.3;
  }
  .partner--listing { left: 172px; width: 68px; height: 65px; background: var(--badge-grey); }
  .partner--maker { left: 270px; width: 66px; height: 66px; background: var(--brand-red); }
  .partner--certified { left: 375px; width: 66px; height: 64px; top: 22px; }
</style>
</head>
<body>
  <main class="flyer">
    <div class="hero-photo" role="img" aria-label="Photo of a house with a dark tiled roof and wooden gable against a blue sky"></div>

    <div class="brand-flag">
      <svg viewBox="0 0 108 147" width="108" height="147" aria-hidden="true">
        <polygon points="0,0 108,0 108,117 0,147" fill="var(--brand-red)"/>
      </svg>
      <div class="brand-name">MARROWIND<br>EXTERIORS</div>
    </div>

    <h1 class="headline">BUY<br>A NEW<br>ROOF</h1>

    <svg class="exclaim" viewBox="0 0 46 171" aria-hidden="true">
      <polygon points="0,0 46,0 39,111 8,111" fill="var(--white)"/>
      <ellipse cx="23" cy="146" rx="23" ry="25" fill="var(--white)"/>
    </svg>

    <svg class="price-seal" viewBox="0 0 142 142" aria-label="Price $17,997.">
      <circle cx="71" cy="71" r="71" fill="var(--brand-red)"/>
      <circle cx="71" cy="71" r="58" fill="var(--brand-green)"/>
      <g transform="rotate(16 71 71)" font-family="Montserrat, sans-serif" font-weight="800" text-anchor="middle">
        <text x="73" y="68" font-size="28" fill="var(--brand-red)">Price</text>
        <text x="71" y="90" font-size="19" fill="var(--white)">$17,997.</text>
      </g>
    </svg>

    <div class="rule rule--upper"></div>
    <p class="offer">and receive a <strong>free gutter<br>replacement,</strong> and <strong>10 years<br>of free roof maintenance.</strong></p>
    <div class="rule rule--lower"></div>

    <p class="warranty">with added <strong>50 year warranty</strong><br>&amp; <strong>25 year workmanship warranty.</strong></p>

    <footer class="partner-strip">
      <div class="partner partner--brand">MARROWIND<br>EXTERIORS</div>
      <div class="partner partner--listing" role="img" aria-label="Business accreditation badge"></div>
      <div class="partner partner--maker" role="img" aria-label="Roofing manufacturer badge"></div>
      <svg class="partner partner--certified" viewBox="0 0 66 64" role="img" aria-label="Certified contractor badge">
        <polygon points="33,0 66,32 33,64 0,32" fill="var(--badge-gold)"/>
        <polygon points="33,4 62,32 33,60 4,32" fill="var(--badge-navy)"/>
      </svg>
    </footer>
  </main>
</body>
</html>
```